Modern Mortgage company wants to attract best professionals Business Card

We need a business card design for a growing innovative modern mortgage company. we would like to see designs that are attractive and functional possibly integrating individual QR codes and head shots. please integrate the color blue. The final design should communicate a sense speed and trust. a subtle integration of a hawaii elements

Industry/Entity Type

Mortgage Brokerage

Contact Information for Business Card

Please have room for Company information(Logo, name, nmls id number, address, phone,URL ), EMployee contact info( headshot, name, NMLS number, title,

Logo Text

Brightpath Home Loans

Colors
3276b5
33a6d7
0692cd
85cae6
85acd3
0455a3

Requirements
Must have
• Please have room for Company information(Logo, name, nmls id number, address, phone,URL ), EMployee contact info(name, NMLS number, title, phone, email, fax, URL)
Nice to have
• Employee Headshot, and QR code

```html
<!DOCTYPE html>
<html lang="en">
<head>
<meta charset="utf-8">
<title>Brightpath Home Loans — Business Card</title>
<link href="https://fonts.googleapis.com/css2?family=Open+Sans:wght@400;600&display=swap" rel="stylesheet">
<style>
  :root {
    --navy: #14335c;
    --sky: #58a3d6;
    --stone: #b3b4b6;
    --ink: #5a5a5a;
    --paper: #ffffff;
  }
  html, body {
    margin: 0;
    width: 1200px;
    height: 1176px;
    overflow: hidden;
    background: var(--paper);
    font-family: "Open Sans", Arial, sans-serif;
  }
  .card {
    position: absolute;
    left: 312px;
    top: 321px;
    width: 581px;
    height: 372px;
    background: var(--paper);
    outline: 1px solid #e4e4e4;
    overflow: hidden;
  }
  .card-shapes {
    position: absolute;
    inset: 0;
  }
  .brand-name {
    position: absolute;
    left: 20px;
    top: 78px;
    width: 190px;
    text-align: center;
    color: var(--navy);
    font-weight: 600;
    font-size: 24px;
    line-height: 1.25;
  }
  .person {
    position: absolute;
    right: 26px;
    top: 85px;
    text-align: left;
    width: 180px;
  }
  .person-name {
    color: var(--paper);
    font-weight: 600;
    font-size: 19px;
    letter-spacing: 0.5px;
    line-height: 1;
  }
  .person-title {
    margin-top: 9px;
    color: var(--sky);
    font-size: 13px;
    letter-spacing: 2.6px;
  }
  .phones {
    position: absolute;
    left: 28px;
    top: 270px;
  }
  .contacts {
    position: absolute;
    right: 20px;
    top: 247px;
  }
  .line {
    display: flex;
    align-items: center;
    gap: 10px;
    height: 25px;
    color: var(--ink);
    font-size: 16px;
    letter-spacing: 0.6px;
  }
  .contacts .line {
    justify-content: flex-end;
    gap: 20px;
    height: 26px;
    font-size: 17px;
    letter-spacing: 0.2px;
  }
  .icon { width: 16px; height: 16px; flex: none; }
</style>
</head>
<body>
  <div class="card">
    <svg class="card-shapes" width="581" height="372" viewBox="0 0 581 372">
      <rect class="top-band" x="0" y="0" width="215" height="37" fill="var(--sky)"/>
      <polygon class="header-panel" points="233,0 581,0 581,159 300,159" fill="var(--navy)"/>
      <polygon class="accent-wedge" points="315,159 370,159 333,236" fill="var(--sky)"/>
      <polygon class="speed-stripe" points="193,0 233,0 333,236 291,230" fill="var(--stone)"/>
      <polygon class="footer-stone" points="0,328 240,328 261,372 0,372" fill="var(--stone)"/>
      <polygon class="footer-sky" points="240,328 581,328 581,372 261,372" fill="var(--sky)"/>
    </svg>

    <div class="brand-name">Brightpath<br>Home Loans</div>

    <div class="person">
      <div class="person-name">PERSONS NAME</div>
      <div class="person-title">PERSONS TITLE</div>
    </div>

    <div class="phones">
      <div class="line">
        <svg class="icon" viewBox="0 0 16 16"><path d="M3.5 1.5l2.5 0 1 3.5-1.6 1.2a8 8 0 0 0 4.4 4.4L11 9l3.5 1v2.5c0 1-1 2-2 2A11 11 0 0 1 1.5 3.5c0-1 1-2 2-2z" fill="var(--sky)"/></svg>
        <span>(999) 222-5555</span>
      </div>
      <div class="line">
        <svg class="icon" viewBox="0 0 16 16"><rect x="4" y="1" width="8" height="14" rx="1.5" fill="none" stroke="var(--sky)" stroke-width="1.6"/><rect x="7" y="12" width="2" height="1.2" fill="var(--sky)"/></svg>
        <span>(999) 222-4444</span>
      </div>
    </div>

    <div class="contacts">
      <div class="line">
        <span>aaaaaaa@nnn.com</span>
        <svg class="icon" viewBox="0 0 16 16"><rect x="1.5" y="4" width="13" height="8.5" fill="var(--sky)"/><path d="M1.5 4.5l6.5 4.5 6.5-4.5" fill="none" stroke="#fff" stroke-width="1"/></svg>
      </div>
      <div class="line">
        <span>City, State Name, 77</span>
        <svg class="icon" viewBox="0 0 16 16"><path d="M8 1a5 5 0 0 0-5 5c0 3.8 5 9 5 9s5-5.2 5-9a5 5 0 0 0-5-5z" fill="var(--sky)"/><circle cx="8" cy="6" r="2" fill="#fff"/></svg>
      </div>
      <div class="line">
        <span>www.sssssssss.com</span>
        <svg class="icon" viewBox="0 0 16 16"><circle cx="8" cy="8" r="6.3" fill="var(--sky)"/><path d="M1.8 8h12.4M8 1.7c-3 3.5-3 9.1 0 12.6M8 1.7c3 3.5 3 9.1 0 12.6M3 4.8h10M3 11.2h10" fill="none" stroke="#fff" stroke-width="0.8"/></svg>
      </div>
    </div>
  </div>
</body>
</html>
```